new letterhead/envelope/business card design for law firm

please see attached pdf of current letterhead, envelope and business card. I am also attaching my new logo that I would like to be used. basically, I am looking to refresh and simplify my letterhead/stationary and business card, keeping the following in mind:

overall, I am going for the following look:

-simple,
-modern,
-classy,
-professional

Target Market(s)

law firm clients

Industry/Entity Type

Law Firm

Contact Information for Business Card

see attachment

Font styles to use
Sans Serif

Requirements
Must have
• overall, I am going for the following look:
• -simple,
• -modern,
• -classy,
• -professional
Nice to have
• same as above
Should not have
• no serif fonts

```html
<!DOCTYPE html>
<html lang="en">
<head>
<meta charset="utf-8">
<title>Calloway Law Stationery</title>
<link href="https://fonts.googleapis.com/css2?family=Montserrat:wght@600;700&family=Open+Sans:wght@400;600&display=swap" rel="stylesheet">
<style>
  :root{
    --backdrop:#c8c9ca;
    --paper:#ffffff;
    --navy:#1f3358;
    --green:#4f8a3a;
    --ink:#3a3f47;
    --shadow:rgba(0,0,0,.18);
  }
  *{margin:0;padding:0;box-sizing:border-box}
  html,body{width:1200px;height:986px;overflow:hidden}
  body{background:var(--backdrop);font-family:"Open Sans",Arial,sans-serif;color:var(--ink);position:relative}
  .sheet{position:absolute;background:var(--paper);box-shadow:0 6px 18px var(--shadow)}

  .brand{display:flex;align-items:center;gap:8px}
  .brand-dot{flex:none;border-radius:50%;background:var(--navy)}
  .brand-name{font-family:"Montserrat",Arial,sans-serif;font-weight:700;color:var(--navy);letter-spacing:.04em;white-space:nowrap}

  /* Letterhead */
  .letterhead{left:650px;top:40px;width:480px;height:621px}
  .letterhead .brand{position:absolute;left:34px;top:34px}
  .letterhead .brand-dot{width:26px;height:26px}
  .letterhead .brand-name{font-size:17px}
  .letterhead-footer{position:absolute;left:34px;right:34px;bottom:30px;border-top:2px solid var(--green);padding-top:7px;display:flex;justify-content:space-between;font-size:9px;line-height:1.45}
  .footer-address .label{color:var(--green)}
  .footer-credentials{text-align:right;color:var(--navy)}

  /* Business card */
  .business-card{left:190px;top:300px;width:280px;height:160px;padding:18px}
  .card-holder{position:absolute;right:18px;top:18px;text-align:right}
  .card-holder .name{font-weight:600;font-size:10px;color:var(--navy)}
  .card-holder .license{font-size:7.5px}
  .business-card .brand{position:absolute;left:18px;top:72px}
  .business-card .brand-dot{width:18px;height:18px}
  .business-card .brand-name{font-size:12px}
  .card-address{position:absolute;left:44px;top:96px;font-size:6.5px;line-height:1.4}
  .card-contact{position:absolute;right:18px;top:62px;text-align:right;font-size:6.5px;line-height:1.45}
  .card-contact .label{color:var(--green);font-weight:600}
  .card-contact .web{margin-top:6px}

  /* Envelope */
  .envelope{left:60px;top:560px;width:560px;height:290px}
  .envelope .brand{position:absolute;left:34px;top:34px}
  .envelope .brand-dot{width:30px;height:30px}
  .envelope .brand-name{font-size:18px}
  .return-address{position:absolute;left:72px;top:70px;font-size:10px;font-weight:600;color:var(--navy);line-height:1.4}
</style>
</head>
<body>

<section class="sheet letterhead" aria-label="Letterhead">
  <div class="brand"><span class="brand-dot"></span><span class="brand-name">CALLOWAY LAW</span></div>
  <footer class="letterhead-footer">
    <div class="footer-address">
      2240 Harlow Lane, Suite 410 Raleigh, NC 27612<br>
      <span class="label">Tel</span> 919.555.0142 | <span class="label">Fax</span> 919.555.0178
    </div>
    <div class="footer-credentials">
      DANIEL R. CALLOWAY, ESQ. | Licensed in NC and FL<br>
      Board Certified in Civil Trial Law by NTCB
    </div>
  </footer>
</section>

<section class="sheet business-card" aria-label="Business card">
  <div class="card-holder">
    <div class="name">DANIEL R. CALLOWAY, ESQ.</div>
    <div class="license">Licensed in NC and FL</div>
  </div>
  <div class="brand"><span class="brand-dot"></span><span class="brand-name">CALLOWAY LAW</span></div>
  <div class="card-address">2240 Harlow Lane, Suite 410<br>Raleigh, NC 27612</div>
  <div class="card-contact">
    <div><span class="label">Tel</span> 919.555.0142</div>
    <div><span class="label">Fax</span> 919.555.0178</div>
    <div><span class="label">Cell</span> 919.555.0193</div>
    <div class="web">www.callowaylawpa.com</div>
    <div>dan@callowaylawpa.com</div>
  </div>
</section>

<section class="sheet envelope" aria-label="Envelope">
  <div class="brand"><span class="brand-dot"></span><span class="brand-name">CALLOWAY LAW</span></div>
  <div class="return-address">2240 Harlow Lane, Suite 410<br>Raleigh, NC 27612</div>
</section>

</body>
</html>
```